TESOL in Vietnam

My company needs banner ad designs (5 different sizes) to be placed on various websites to promote our product.

Our product is a 4-week Teaching English to Speakers of other Languages (TESOL) training program in Ho Chi Minh City, Vietnam. TESOL certification is the minimum qualification to work as an English language teacher in many parts of the world.

Basically, we want people to enroll in our 4 week Teacher training course in HCMC, Vietnam, with the view of teaching English in Vietnam.

You can see who we are and what we do here: www.lumarocraft-learning.com

Key pointers include:

1. Our company logo (which includes our name & slogan) will be prominent in the banner - see attached

2. Our website address will be prominent:
www.lumarocraft-learning.com

3. The main selling points for our product will be listed in the banner - note below:

Our TESOL training program in Ho Chi Minh City, Vietnam includes:

- the 4-week TESOL course (Australian Government accredited, internationally recognised);
- western standard accommodation within a 4 minute walk of my school for the duration of the course (4-weeks); and
- a guaranteed English teaching position at the end, paid at market rates.

4. the color scheme should be bright and eye catching - a lot of red, orange and alike.

I hope this information is helpful.

Dalton Wrexby

Hi All Note the rough sketch that I have added to the brief associated with this project. Cheers Dalton

Target Market(s)

Men & women - 22 to 35 years of aage
Adventurous
Love to travel

Industry/Entity Type

Accommodation

Other font styles liked:
• Calibri

Colors
eb1f27

Requirements
Must have
• Sense of fun
Credibility
Nice to have
• bright colors
Should not have
• Dour

```html
<!DOCTYPE html>
<html lang="en">
<head>
<meta charset="utf-8">
<title>TESOL in Vietnam – Banner Set</title>
<link rel="stylesheet" href="https://fonts.googleapis.com/css2?family=Carlito:wght@400;700&family=Arimo&display=swap">
<style>
  :root {
    --brand-red: #d0021b;
    --accent-yellow: #ffe800;
    --ink: #111111;
    --label-grey: #444444;
    --frame-grey: #555555;
    --paper: #ffffff;
  }
  * { box-sizing: border-box; margin: 0; padding: 0; }
  html, body { width: 1200px; height: 1000px; overflow: hidden; background: var(--paper); }
  .sheet { position: relative; width: 1200px; height: 1000px; font-family: "Carlito", "Calibri", sans-serif; }

  .size-label {
    position: absolute; left: 0; width: 1200px; text-align: center;
    font-family: "Arimo", Arial, sans-serif; font-size: 24px; color: var(--label-grey);
  }
  .banner { position: absolute; border: 1px solid var(--frame-grey); background: var(--paper); }

  .brand { position: absolute; display: flex; align-items: center; gap: 10px; }
  .brand-dot { flex: none; border-radius: 50%; background: var(--brand-red); }
  .brand-name { color: var(--brand-red); font-weight: 700; line-height: 1.05; }

  .headline { position: absolute; color: var(--brand-red); font-weight: 700; white-space: nowrap; line-height: 1; }

  .red-panel {
    position: absolute; background: var(--brand-red); color: var(--paper);
    display: flex; align-items: center; justify-content: center; text-align: center;
    font-weight: 700; font-size: 60px; line-height: 0.85;
  }

  .perk {
    position: absolute; background: var(--paper);
    border: 4px solid var(--accent-yellow); border-radius: 6px;
    box-shadow: 0 5px 0 var(--brand-red);
    display: flex; align-items: center; justify-content: center; text-align: center;
    color: var(--ink); font-weight: 700; line-height: 1.1;
  }
</style>
</head>
<body>
<main class="sheet">

  <!-- Leaderboard -->
  <div class="size-label" style="top:58px;">468x60 &amp; 728x90</div>
  <section class="banner" style="left:0; top:94px; width:1200px; height:154px;">
    <div class="brand" style="left:40px; top:45px;">
      <span class="brand-dot" style="width:36px; height:36px;"></span>
      <span class="brand-name" style="font-size:30px;">Lumarocraft<br>Learning</span>
    </div>
    <div class="red-panel" style="left:353px; top:0; width:258px; height:152px;">TESOL<br>in<br>Vietnam</div>
    <div class="perk" style="left:632px; top:38px; width:173px; height:68px; font-size:15px;">Australian Government<br>accredited</div>
    <div class="perk" style="left:812px; top:38px; width:173px; height:68px; font-size:15px;">Free Accomodation in<br>Ho Chi Minh City</div>
    <div class="perk" style="left:993px; top:38px; width:173px; height:68px; font-size:15px;">Guaranteed Teaching<br>job at the end</div>
  </section>

  <!-- Half banner -->
  <div class="size-label" style="top:258px;">234x60</div>
  <section class="banner" style="left:257px; top:289px; width:685px; height:176px;">
    <div class="brand" style="left:22px; top:60px;">
      <span class="brand-dot" style="width:30px; height:30px;"></span>
      <span class="brand-name" style="font-size:26px;">Lumarocraft<br>Learning</span>
    </div>
    <div class="headline" style="left:277px; top:32px; font-size:50px;">TESOL in Vietnam</div>
    <div class="perk" style="left:278px; top:87px; width:126px; height:50px; font-size:11px;">Australian Government<br>accredited</div>
    <div class="perk" style="left:408px; top:87px; width:127px; height:50px; font-size:11px;">Free Accomodation in<br>Ho Chi Minh City</div>
    <div class="perk" style="left:540px; top:87px; width:125px; height:50px; font-size:11px;">Guaranteed Teaching<br>job at the end</div>
  </section>

  <!-- Full banner -->
  <div class="size-label" style="top:478px;">600x120</div>
  <section class="banner" style="left:253px; top:508px; width:687px; height:138px;">
    <div class="brand" style="left:24px; top:42px;">
      <span class="brand-dot" style="width:30px; height:30px;"></span>
      <span class="brand-name" style="font-size:26px;">Lumarocraft<br>Learning</span>
    </div>
    <div class="headline" style="left:271px; top:18px; font-size:50px;">TESOL in Vietnam</div>
    <div class="perk" style="left:269px; top:66px; width:127px; height:50px; font-size:11px;">Australian Government<br>accredited</div>
    <div class="perk" style="left:400px; top:66px; width:127px; height:50px; font-size:11px;">Free Accomodation in<br>Ho Chi Minh City</div>
    <div class="perk" style="left:531px; top:66px; width:126px; height:50px; font-size:11px;">Guaranteed Teaching<br>job at the end</div>
  </section>

  <!-- Medium rectangle -->
  <div class="size-label" style="top:656px;">300x250</div>
  <section class="banner" style="left:428px; top:688px; width:375px; height:312px;">
    <div class="brand" style="left:88px; top:60px;">
      <span class="brand-dot" style="width:30px; height:30px;"></span>
      <span class="brand-name" style="font-size:26px;">Lumarocraft<br>Learning</span>
    </div>
    <div class="headline" style="left:0; width:373px; text-align:center; top:180px; font-size:42px;">TESOL in Vietnam</div>
    <div class="perk" style="left:21px; top:228px; width:109px; height:43px; font-size:9px;">Australian Government<br>accredited</div>
    <div class="perk" style="left:133px; top:228px; width:109px; height:43px; font-size:9px;">Free Accomodation in<br>Ho Chi Minh City</div>
    <div class="perk" style="left:245px; top:228px; width:109px; height:43px; font-size:9px;">Guaranteed Teaching<br>job at the end</div>
  </section>

</main>
</body>
</html>
```